Banner for conference

I have 3 very simple banner designs that I would like jazzed up a little. I really do want to keep them simple, so it may only be a font and layout change you recommend.
The banners are for daltrix.com, with our new slogan 'Send it with Daltrix', and 'Send. Sign. Store.' or 'I send. You sign. We store.'
Size of banner - 830mm x 2000mm (Exhibition banners)

I would prefer to have the solid colour and white writing, but open to suggestions.

Target Market(s)

Target customers are mainly schools at this stage, but we will also attend KovEX, where we will be talking to other software companies to discuss the option for them to integrate Daltrix into their solution.

Industry/Entity Type

Store

Requirements
Must have
• solid colours

```html
<!DOCTYPE html>
<html lang="en">
<head>
<meta charset="utf-8">
<title>Daltrix – Exhibition Banners</title>
<link rel="stylesheet" href="https://fonts.googleapis.com/css2?family=Didact+Gothic&display=swap">
<style>
  :root {
    --canvas: #ffffff;
    --banner-red: #e01e4c;
    --band-red: #b8173f;
    --ink: #ffffff;
    --font: "Didact Gothic", "Century Gothic", sans-serif;
  }
  * { box-sizing: border-box; margin: 0; padding: 0; }
  html, body {
    width: 1200px;
    height: 1000px;
    overflow: hidden;
    background: var(--canvas);
  }
  .canvas {
    position: relative;
    width: 1200px;
    height: 1000px;
    font-family: var(--font);
    color: var(--ink);
  }
  .banner {
    position: absolute;
    top: 191px;
    width: 256px;
    height: 616px;
    background: var(--banner-red);
    overflow: hidden;
  }
  .banner--send-with { left: 156px; }
  .banner--send-sign-store { left: 472px; }
  .banner--i-send { left: 788px; }

  .banner__band {
    position: absolute;
    left: 0;
    top: 0;
    width: 256px;
    height: 616px;
  }
  .banner__band polygon { fill: var(--band-red); }

  .brand {
    position: absolute;
    left: 35px;
    top: 31px;
    display: flex;
    align-items: center;
    gap: 10px;
  }
  .brand__dot {
    width: 76px;
    height: 76px;
    border-radius: 50%;
    background: var(--ink);
  }
  .brand__name {
    font-size: 36px;
    line-height: 1;
    letter-spacing: -0.5px;
  }

  .slogan {
    position: absolute;
    font-weight: 400;
    line-height: 1;
  }
  .slogan span { display: block; white-space: nowrap; }

  .banner--send-with .slogan { left: 45px; top: 229px; }
  .banner--send-with .slogan__lead { font-size: 64px; }
  .banner--send-with .slogan__mid { font-size: 42px; margin-top: 2px; }
  .banner--send-with .slogan__tail { font-size: 38px; margin-top: 8px; }

  .banner--send-sign-store .slogan { left: 66px; top: 226px; font-size: 50px; }
  .banner--send-sign-store .slogan span + span { margin-top: 6px; }

  .banner--i-send .slogan { left: 32px; top: 225px; font-size: 48px; }
  .banner--i-send .slogan span + span { margin-top: 6px; }
  .banner--i-send .slogan span:last-child { margin-top: 12px; }

  .banner__url {
    position: absolute;
    left: 0;
    right: 0;
    top: 566px;
    text-align: center;
    font-size: 23px;
    letter-spacing: 0.2px;
  }
</style>
</head>
<body>
<main class="canvas">

  <section class="banner banner--send-with">
    <svg class="banner__band" viewBox="0 0 256 616" aria-hidden="true">
      <polygon points="0,141 256,233 256,476 0,384"/>
    </svg>
    <div class="brand"><span class="brand__dot"></span><span class="brand__name">Daltrix</span></div>
    <p class="slogan">
      <span class="slogan__lead">Send</span>
      <span class="slogan__mid">it with</span>
      <span class="slogan__tail">Daltrix</span>
    </p>
    <p class="banner__url">www.daltrix.com</p>
  </section>

  <section class="banner banner--send-sign-store">
    <svg class="banner__band" viewBox="0 0 256 616" aria-hidden="true">
      <polygon points="0,141 256,233 256,476 0,384"/>
    </svg>
    <div class="brand"><span class="brand__dot"></span><span class="brand__name">Daltrix</span></div>
    <p class="slogan">
      <span>Send</span>
      <span>Sign</span>
      <span>Store</span>
    </p>
    <p class="banner__url">www.daltrix.com</p>
  </section>

  <section class="banner banner--i-send">
    <svg class="banner__band" viewBox="0 0 256 616" aria-hidden="true">
      <polygon points="0,141 256,233 256,476 0,384"/>
    </svg>
    <div class="brand"><span class="brand__dot"></span><span class="brand__name">Daltrix</span></div>
    <p class="slogan">
      <span>I send</span>
      <span>You sign</span>
      <span>I store</span>
    </p>
    <p class="banner__url">www.daltrix.com</p>
  </section>

</main>
</body>
</html>
```